Naturopath Practitioner Card Design

I am a naturopath needing a design for a business card mainly to show that I am a naturopath and have some contact details to give to prospective clients. I am open minded about the design and what is on the second side of the card whether it just be some artwork or space for details, appointment times etc. Naturopathy is the practice of natural medicine that uses a holistic approach and incorporates herbal and nutritional medicine.

Contact Information for Business Card

Tom Waverly NaturopathBHSc (Naturopathy) Member NHPG 0491 582 736 tom.waverly@mailbox-example.net www.tomwaverlynaturopathy.example.au

Requirements
Nice to have
• Would prefer some kind of original pattern/art work/logo rather than an image, not fussed if its very simple/basic
• I am open to any colour but think I would prefer a more earthy sandy clay etc type style than the greens that are commonly associated with naturopathy.
Should not have
• Don't really want to have generic stock images on it

```html
<!DOCTYPE html>
<html lang="en">
<head>
<meta charset="utf-8">
<title>Tom Waverly Naturopathy – Business Card</title>
<link rel="stylesheet" href="https://fonts.googleapis.com/css2?family=Cinzel:wght@400&family=Open+Sans:wght@400;600&display=swap">
<style>
  :root {
    --page-bg: #e9e6e1;
    --card-white: #ffffff;
    --brand-green: #718c3f;
    --ink: #333333;
    --rule: #b5b5b5;
    --on-green: #ffffff;
  }
  html, body {
    margin: 0;
    padding: 0;
    width: 1200px;
    height: 1000px;
    overflow: hidden;
    background: var(--page-bg);
  }
  .canvas {
    position: relative;
    width: 1200px;
    height: 1000px;
  }
  .card {
    position: absolute;
    left: 265px;
    width: 666px;
    height: 397px;
    box-shadow: 0 4px 12px rgba(0,0,0,0.18);
    overflow: hidden;
  }
  .card--front { top: 73px; background: var(--card-white); }
  .card--back { top: 532px; background: var(--brand-green); }

  .wordmark {
    position: absolute;
    font-family: "Cinzel", serif;
    font-weight: 400;
    text-align: center;
  }
  .wordmark__name { display: block; white-space: nowrap; }
  .wordmark__trade { display: block; white-space: nowrap; }
  .wordmark__dot {
    display: block;
    border-radius: 50%;
    margin: 0 auto;
  }

  .card--front .wordmark {
    left: 20px;
    top: 40px;
    width: 330px;
    color: var(--ink);
  }
  .card--front .wordmark__dot {
    width: 64px; height: 64px;
    background: var(--brand-green);
    margin-bottom: 34px;
  }
  .card--front .wordmark__name { font-size: 40px; line-height: 46px; }
  .card--front .wordmark__trade { font-size: 22px; line-height: 30px; letter-spacing: 1px; }

  .practitioner {
    position: absolute;
    right: 32px;
    top: 228px;
    text-align: right;
    font-family: "Open Sans", sans-serif;
  }
  .practitioner__name {
    color: var(--brand-green);
    font-weight: 600;
    font-size: 21px;
    line-height: 28px;
  }
  .practitioner__cred { font-size: 15px; font-weight: 400; }
  .practitioner__role {
    color: var(--ink);
    font-size: 17px;
    line-height: 26px;
  }
  .divider {
    position: absolute;
    left: 33px;
    top: 269px;
    width: 478px;
    height: 1px;
    background: linear-gradient(to right, rgba(181,181,181,0.3), var(--rule) 60%, #888);
  }

  .contact {
    position: absolute;
    left: 33px;
    top: 296px;
    margin: 0;
    padding: 0;
    list-style: none;
    font-family: "Open Sans", sans-serif;
    font-size: 16.5px;
    color: var(--ink);
  }
  .contact__item {
    display: flex;
    align-items: center;
    height: 26px;
  }
  .contact__icon {
    width: 14px;
    height: 14px;
    margin-right: 9px;
    fill: var(--brand-green);
  }

  .card--back .wordmark {
    left: 0;
    top: 90px;
    width: 666px;
    color: var(--on-green);
  }
  .card--back .wordmark__dot {
    width: 84px; height: 84px;
    background: var(--on-green);
    margin-bottom: 38px;
  }
  .card--back .wordmark__name { font-size: 56px; line-height: 62px; }
  .card--back .wordmark__trade { font-size: 28px; line-height: 38px; letter-spacing: 1px; }
</style>
</head>
<body>
<main class="canvas">
  <section class="card card--front" aria-label="Card front">
    <div class="wordmark">
      <span class="wordmark__dot" aria-hidden="true"></span>
      <span class="wordmark__name">Tom Waverly</span>
      <span class="wordmark__trade">Naturopathy</span>
    </div>

    <div class="practitioner">
      <div class="practitioner__name">TOM WAVERLY <span class="practitioner__cred">BHSc</span></div>
      <div class="practitioner__role">Naturopathy</div>
    </div>
    <div class="divider"></div>

    <ul class="contact">
      <li class="contact__item">
        <svg class="contact__icon" viewBox="0 0 16 16" aria-hidden="true"><path d="M1 6c0-2 3-3 7-3s7 1 7 3v1h-3.5V5.5h-7V7H1z M3 8h10l1.5 5h-13z M6 9.5h4v2H6z"/></svg>
        0491 582 736
      </li>
      <li class="contact__item">
        <svg class="contact__icon" viewBox="0 0 16 16" aria-hidden="true"><path d="M1 4h14v1L8 9.5 1 5z M1 6.5l7 4.5 7-4.5V12H1z"/></svg>
        tom.waverly@mailbox-example.net
      </li>
      <li class="contact__item">
        <svg class="contact__icon" viewBox="0 0 16 16" aria-hidden="true"><circle cx="8" cy="8" r="7"/><path d="M4 5c2 0 2 2 4 2s1 3-1 3-1 3-2 3" fill="none" stroke="#fff" stroke-width="1.2"/></svg>
        www.tomwaverlynaturopathy.example.au
      </li>
    </ul>
  </section>

  <section class="card card--back" aria-label="Card back">
    <div class="wordmark">
      <span class="wordmark__dot" aria-hidden="true"></span>
      <span class="wordmark__name">Tom Waverly</span>
      <span class="wordmark__trade">Naturopathy</span>
    </div>
  </section>
</main>
</body>
</html>
```